Carton Box Packaging For Motorcycle Electric Regulator - Verosta Brand

Packaging Dimensions: 7cm (H) x 6cm (W) x 2.5cm (D)
We would like to design a genuine Carton box Packaging for motorcycle electric regulator.
This is a sensitive part of the motorcycle, so we need the packaging to reflect elegant impression.
Verosta, is one of the leading companies for manufacturing Motorcycles, located in Egypt. Our company is offering high-quality products, the best in the local market, with very competitive prices.
We have a limited time to get this project done, So we Highly appreciate receiving your designs ASAP.
Target Market(s)
Motorcycle Parts Buyers
Font styles to use
Colors
Designer to choose colors to be used in the design.
Look and feel
Each slider illustrates characteristics of the customer's brand and the style your logo design should communicate.

```html
<!DOCTYPE html>
<html lang="en">
<head>
<meta charset="utf-8">
<title>Verosta Motorcycle Regulator – Box Panels</title>
<link href="https://fonts.googleapis.com/css2?family=Russo+One&family=Oswald:wght@300;400&display=swap" rel="stylesheet">
<style>
  :root {
    --bg: #e6eef3;
    --navy-deep: #06182e;
    --navy: #0b2a4c;
    --blue-glow: #1f6fb8;
    --sky: #4fb4ee;
    --panel-light: #f1f2f4;
    --panel-light-2: #d9dde2;
    --ink: #0d1f33;
    --text-light: #dfe9f2;
    --tile: #e9eaec;
  }
  * { margin: 0; padding: 0; box-sizing: border-box; }
  html, body { width: 1200px; height: 864px; overflow: hidden; }
  body {
    background: var(--bg);
    position: relative;
    font-family: "Oswald", sans-serif;
  }
  .box-net {
    position: absolute;
    left: 175px; top: 82px;
    width: 850px; height: 700px;
    display: flex;
  }
  /* Side panel */
  .side-panel {
    width: 250px; height: 100%;
    background: linear-gradient(180deg, var(--navy) 0%, var(--navy-deep) 60%, #09233f 100%);
    position: relative;
    border-right: 1px solid #04101f;
  }
  .side-panel .brand-tile {
    position: absolute; left: 60px; top: 40px;
    width: 130px; height: 130px;
  }
  .side-title {
    position: absolute; left: 125px; top: 430px;
    transform: translate(-50%, -50%) rotate(90deg);
    font-family: "Russo One", sans-serif;
    color: #ffffff;
    font-size: 34px; line-height: 1.05;
    text-align: left; white-space: nowrap;
  }
  .side-product {
    position: absolute; left: 95px; top: 590px;
    width: 60px; height: 90px;
    border-radius: 6px;
    background: linear-gradient(180deg, #2a3440, #0e141b);
  }
  /* Front panel */
  .front-panel {
    width: 600px; height: 100%;
    position: relative;
    overflow: hidden;
  }
  .front-top {
    position: absolute; inset: 0 0 auto 0; height: 335px;
    background: linear-gradient(180deg, var(--panel-light-2) 0%, var(--panel-light) 45%, #ffffff 100%);
  }
  .brand-tile {
    border-radius: 24px;
    background: linear-gradient(160deg, #ffffff, var(--tile) 60%, #cfd2d6);
    box-shadow: 0 8px 18px rgba(0,0,0,0.25);
    display: flex; align-items: center; justify-content: center;
  }
  .front-top .brand-tile {
    position: absolute; left: 215px; top: 45px;
    width: 170px; height: 170px;
  }
  .brand-name {
    font-family: "Russo One", sans-serif;
    color: var(--ink);
    font-size: 30px;
  }
  .side-panel .brand-name { font-size: 23px; }
  .front-title {
    position: absolute; left: 0; right: 0; top: 262px;
    text-align: center;
    font-family: "Russo One", sans-serif;
    color: var(--ink);
    font-size: 38px;
  }
  .front-bottom {
    position: absolute; inset: 335px 0 0 0;
    background: radial-gradient(ellipse at 75% 45%, var(--blue-glow) 0%, var(--navy) 40%, var(--navy-deep) 85%);
  }
  .product-photo {
    position: absolute; left: 320px; top: 55px;
    width: 250px; height: 260px;
    border-radius: 14px;
    background: radial-gradient(ellipse at 50% 55%, #2b3642 0%, #121a22 60%, rgba(10,20,35,0) 100%);
  }
  .feature-list {
    position: absolute; left: 30px; top: 135px;
    list-style: none;
  }
  .feature-list li {
    display: flex; align-items: center;
    color: var(--text-light);
    font-weight: 300; font-size: 34px;
    line-height: 1; margin-bottom: 20px;
  }
  .feature-list li::before {
    content: "";
    width: 26px; height: 26px; border-radius: 50%;
    margin-right: 18px; flex: none;
    background: radial-gradient(circle at 35% 35%, #bfe6ff, var(--sky) 45%, #1a5f9c);
    box-shadow: 0 0 10px rgba(79,180,238,0.7);
  }
</style>
</head>
<body>
  <div class="box-net">
    <section class="side-panel">
      <div class="brand-tile"><span class="brand-name">Verosta</span></div>
      <h2 class="side-title">Motorcycle<br>Regulator</h2>
      <div class="side-product" role="img" aria-label="Photo of the motorcycle regulator with its wiring"></div>
    </section>
    <section class="front-panel">
      <div class="front-top">
        <div class="brand-tile"><span class="brand-name">Verosta</span></div>
        <h1 class="front-title">Motorcycle Regulator</h1>
      </div>
      <div class="front-bottom">
        <div class="product-photo" role="img" aria-label="Photo of a black finned motorcycle voltage regulator with coloured wires and a white connector"></div>
        <ul class="feature-list">
          <li>Replacement Parts</li>
          <li>Durable &amp; Reliable</li>
          <li>Best Quality</li>
        </ul>
      </div>
    </section>
  </div>
</body>
</html>
```